Elegant Financial Planning Business Card

Clear Harbour Wealth Advisory Pty Ltd requires an elegant business card that communicates simplicity, elegance and trust.
Attached card example of 'Dorvane' is very close to what I am looking for. Looking for black and white card.
Update 24/1/16: The attached Dorvane card is almost exactly what I am looking for. Although it is possible that alternative layouts may interest me, it is considerably more likely that I will proceed with a virtual clone of the "Dorvane' example.
Industry/Entity Type
Financial Planning
Contact Information for Business Card
In black font...
Front Details are (layout as per Paula Dorvane card picture):
Line1 - Name: Simon Walsh
Line 2 - Company: Clear Harbour Wealth Advisory Pty Ltd
Line 3 - Address: Marlow Court 3, Level 14, 58 Tennant Road, Bondi Junction NSW
Line 4
- Phone: 178 526
- Email: advice@chwa-example.com.au
- Site: www.chwa-example.com.au
Back details
1/ logo in position and dimensions as per attached layout
2. Bottom left (in smaller writing).
- Authorised Representative No. 517649
- Clear Harbour Wealth Advisory is a corporate authorised representative of Tidewell Capital Partners Pty Ltd
- ABN 47 318 602 154
- AFSL No. 390817

```html
<!DOCTYPE html>
<html lang="en">
<head>
<meta charset="utf-8">
<title>Clear Harbour Wealth Advisory – Business Card</title>
<link rel="stylesheet" href="https://fonts.googleapis.com/css2?family=Tinos:wght@400;700&display=swap">
<style>
  :root {
    --page-bg: #e9e7e3;
    --card-black: #0d0d0d;
    --card-black-soft: #1c1c1c;
    --band-grey: #2a2a2a;
    --swoosh-grey: #a9a9a9;
    --ink-white: #f2f2f2;
    --ink-soft: #d6d6d6;
    --shadow: rgba(0, 0, 0, 0.28);
  }
  * { box-sizing: border-box; margin: 0; padding: 0; }
  html, body {
    width: 1200px;
    height: 900px;
    overflow: hidden;
    background: var(--page-bg);
    font-family: "Tinos", "Times New Roman", serif;
  }
  .canvas {
    position: relative;
    width: 1200px;
    height: 900px;
  }
  .card {
    position: absolute;
    width: 520px;
    height: 318px;
    border-radius: 3px;
    overflow: hidden;
    background: radial-gradient(ellipse at 55% 30%, var(--card-black-soft), var(--card-black) 75%);
    box-shadow: 0 14px 30px var(--shadow);
    color: var(--ink-white);
  }

  /* Back of card */
  .card-back { left: 60px; top: 150px; }
  .back-content {
    position: absolute;
    inset: 0;
    text-align: center;
    padding-top: 48px;
  }
  .brand-name {
    font-size: 42px;
    font-weight: 400;
    letter-spacing: 1px;
    line-height: 1;
    color: var(--ink-white);
  }
  .brand-sub {
    font-size: 20px;
    font-weight: 400;
    letter-spacing: 2.5px;
    line-height: 1.2;
    color: var(--ink-white);
    margin-top: 2px;
  }
  .legal {
    font-size: 12.5px;
    line-height: 1.3;
    color: var(--ink-soft);
  }
  .legal-rep { margin-top: 30px; }
  .legal-ids { margin-top: 14px; }
  .legal-note { margin-top: 14px; padding: 0 40px; }

  /* Front of card */
  .card-front { left: 620px; top: 420px; }
  .front-shape { position: absolute; inset: 0; }
  .front-logo {
    position: absolute;
    right: 26px;
    top: 30px;
    display: flex;
    flex-direction: column;
    align-items: center;
    gap: 8px;
    color: var(--ink-white);
    font-weight: 400;
    text-align: center;
  }
  .logo-mark {
    width: 46px;
    height: 46px;
    border: 2px solid var(--ink-white);
    border-radius: 50%;
  }
  .logo-name { font-size: 14px; line-height: 1; letter-spacing: 0.5px; }
  .logo-sub { font-size: 8.5px; line-height: 1; margin-top: -5px; }
  .holder {
    position: absolute;
    left: 50px;
    top: 100px;
  }
  .holder-name {
    font-size: 22px;
    font-weight: 700;
    color: var(--ink-white);
  }
  .holder-address {
    margin-top: 12px;
    font-size: 14px;
    line-height: 1.3;
    color: var(--ink-soft);
    width: 270px;
  }
  .contact-list {
    list-style: none;
    margin-top: 12px;
  }
  .contact-item {
    display: flex;
    align-items: center;
    gap: 10px;
    font-size: 14px;
    line-height: 1.4;
    color: var(--ink-soft);
  }
  .contact-icon { width: 11px; height: 11px; flex: none; }
</style>
</head>
<body>
<main class="canvas">

  <section class="card card-back" aria-label="Card back">
    <div class="back-content">
      <div class="brand-name">CLEAR HARBOUR</div>
      <div class="brand-sub">Wealth Advisory Pty Ltd</div>
      <p class="legal legal-rep">Authorised Representative No. 517649</p>
      <p class="legal legal-ids">ABN 47 318 602 154<br>AFSL No. 390817</p>
      <p class="legal legal-note">Clear Harbour Wealth Advisory is a corporate authorised representative of Tidewell Capital Partners Pty Ltd</p>
    </div>
  </section>

  <section class="card card-front" aria-label="Card front">
    <svg class="front-shape" width="520" height="318" viewBox="0 0 520 318" aria-hidden="true">
      <path d="M0 300 C 300 302, 400 240, 520 135 L520 318 L0 318 Z" fill="var(--swoosh-grey)"/>
      <path d="M0 318 C 300 316, 410 256, 520 150 L520 318 Z" fill="var(--band-grey)"/>
    </svg>

    <div class="front-logo">
      <span class="logo-mark"></span>
      <span class="logo-name">CLEAR HARBOUR</span>
      <span class="logo-sub">Wealth Advisory Pty Ltd</span>
    </div>

    <div class="holder">
      <h1 class="holder-name">Simon Walsh</h1>
      <p class="holder-address">Marlow Court 3, Level 14, 58 Tennant Road, Bondi Junction NSW</p>
      <ul class="contact-list">
        <li class="contact-item">
          <svg class="contact-icon" viewBox="0 0 12 12" aria-hidden="true"><path d="M2.5 1 L4.5 1 L5 3.5 L3.8 4.4 C4.5 5.8 6.2 7.5 7.6 8.2 L8.5 7 L11 7.5 L11 9.5 C11 10.5 10 11 9 11 C4.5 10.5 1.5 7.5 1 3 C1 2 1.5 1 2.5 1 Z" fill="currentColor"/></svg>
          178 526
        </li>
        <li class="contact-item">
          <svg class="contact-icon" viewBox="0 0 12 12" aria-hidden="true"><rect x="1" y="2.5" width="10" height="7" fill="currentColor"/><path d="M1 2.5 L6 6.5 L11 2.5" stroke="var(--card-black)" stroke-width="1" fill="none"/></svg>
          advice@chwa-example.com.au
        </li>
        <li class="contact-item">
          <svg class="contact-icon" viewBox="0 0 12 12" aria-hidden="true"><circle cx="6" cy="6" r="5" fill="none" stroke="currentColor" stroke-width="1.2"/><path d="M1 6 H11 M6 1 C3.5 3.5 3.5 8.5 6 11 M6 1 C8.5 3.5 8.5 8.5 6 11" fill="none" stroke="currentColor" stroke-width="0.9"/></svg>
          www.chwa-example.com.au
        </li>
      </ul>
    </div>
  </section>

</main>
</body>
</html>
```